Larkspur Stillness

Logo picture and I want it to say

yoga. meditation. sound healing

small sweet classes

Larkspur-stillness.com

2740 West Hollander Ave Suite K
Alder Bay CA 90417

```html
<!DOCTYPE html>
<html lang="en">
<head>
<meta charset="utf-8">
<title>Larkspur Stillness – Flyer</title>
<link rel="stylesheet" href="https://fonts.googleapis.com/css2?family=Montserrat:wght@400;500;600;700&display=swap">
<style>
  :root {
    --paper: #f2f2f4;
    --ink: #1c1c1c;
    --ink-soft: #444446;
    --charcoal: #373737;
    --band-grey: #cfcfd0;
    --white: #ffffff;
    --rule: #d6d6d8;
    --photo-warm-1: #c9b9ad;
    --photo-warm-2: #6e5c55;
    --photo-cool: #3a3a42;
    --photo-soft-1: #f4f1ee;
    --photo-soft-2: #e7ddd4;
  }
  html, body {
    margin: 0;
    padding: 0;
    overflow: hidden;
    background: var(--white);
  }
  .flyer {
    position: relative;
    width: 742px;
    height: 1200px;
    overflow: hidden;
    background: var(--paper);
    font-family: "Montserrat", sans-serif;
    color: var(--ink);
  }
  .flyer__art {
    position: absolute;
    inset: 0;
  }
  .services {
    position: absolute;
    left: 388px;
    top: 550px;
    width: 293px;
    height: 363px;
    box-sizing: border-box;
    border: 3px dotted var(--ink-soft);
    border-radius: 6px;
    text-align: center;
    font-weight: 500;
    letter-spacing: 2px;
    font-size: 29px;
    line-height: 1.15;
  }
  .services__item {
    position: absolute;
    left: 0;
    right: 0;
    margin: 0;
  }
  .services__item--yoga { top: 42px; }
  .services__item--meditation { top: 140px; }
  .services__item--sound { top: 245px; }
  .services__rule {
    position: absolute;
    left: 70px;
    right: 70px;
    height: 1px;
    background: var(--rule);
  }
  .services__rule--one { top: 108px; }
  .services__rule--two { top: 210px; }
  .tagline {
    position: absolute;
    left: 388px;
    width: 293px;
    top: 950px;
    margin: 0;
    text-align: center;
    font-weight: 700;
    font-size: 22px;
    letter-spacing: 2px;
    line-height: 1.3;
    color: var(--ink-soft);
  }
  .logo {
    position: absolute;
    left: 56px;
    top: 303px;
    width: 310px;
    height: 310px;
    display: flex;
    flex-direction: column;
    align-items: center;
    justify-content: center;
    text-align: center;
    font-weight: 500;
    font-size: 30px;
    line-height: 1.15;
    color: var(--ink-soft);
    margin: 0;
  }
  .address {
    position: absolute;
    left: 60px;
    top: 1115px;
    margin: 0;
    font-size: 16px;
    line-height: 1.35;
    font-style: normal;
    color: var(--ink);
  }
  .cta {
    position: absolute;
    right: 37px;
    top: 1113px;
    margin: 0;
    text-align: right;
    color: var(--white);
  }
  .cta__label {
    display: block;
    font-weight: 700;
    font-size: 17px;
    letter-spacing: 1px;
  }
  .cta__url {
    display: block;
    font-size: 17px;
    letter-spacing: 0.5px;
    margin-top: 2px;
  }
</style>
</head>
<body>
<main class="flyer">
  <svg class="flyer__art" width="742" height="1200" viewBox="0 0 742 1200" xmlns="http://www.w3.org/2000/svg">
    <defs>
      <linearGradient id="studio-tones" x1="0" y1="0" x2="1" y2="1">
        <stop offset="0" stop-color="var(--photo-cool)"/>
        <stop offset="0.45" stop-color="var(--photo-warm-2)"/>
        <stop offset="0.8" stop-color="var(--photo-warm-1)"/>
        <stop offset="1" stop-color="var(--photo-warm-2)"/>
      </linearGradient>
      <radialGradient id="meditation-tones" cx="0.45" cy="0.55" r="0.65">
        <stop offset="0" stop-color="var(--photo-soft-2)"/>
        <stop offset="0.7" stop-color="var(--photo-soft-1)"/>
        <stop offset="1" stop-color="var(--paper)" stop-opacity="0"/>
      </radialGradient>
    </defs>

    <path role="img" aria-label="Photo of a group class seated in a bright studio, hands at heart in prayer pose"
          d="M0 0 H742 V280 C560 345 380 400 0 420 Z" fill="url(#studio-tones)"/>

    <path d="M0 410 C380 395 560 340 742 270 V335 C560 410 380 455 0 462 Z" fill="var(--charcoal)"/>

    <rect role="img" aria-label="Photo of a woman in white meditating cross-legged in a soft, bright room"
          x="0" y="540" width="440" height="560" fill="url(#meditation-tones)"/>

    <circle cx="211" cy="458" r="155" fill="var(--white)"/>
    <circle cx="211" cy="458" r="127" fill="none" stroke="var(--ink-soft)" stroke-width="3"/>

    <path d="M0 1097 L400 1085 L330 1200 H0 Z" fill="var(--band-grey)"/>
    <path d="M322 1200 C420 1110 520 1060 742 1052 V1200 Z" fill="var(--white)"/>
    <path d="M336 1200 C430 1118 530 1068 742 1062 V1200 Z" fill="var(--charcoal)"/>
  </svg>

  <p class="logo"><span>Larkspur</span><span>Stillness</span></p>

  <section class="services" aria-label="Classes offered">
    <p class="services__item services__item--yoga">YOGA</p>
    <span class="services__rule services__rule--one"></span>
    <p class="services__item services__item--meditation">MEDITATION</p>
    <span class="services__rule services__rule--two"></span>
    <p class="services__item services__item--sound">SOUND<br>HEALING</p>
  </section>

  <p class="tagline">SMALL SWEET<br>CLASSES</p>

  <address class="address">2740 West Hollander Ave Suite K<br>Alder Bay CA 90417</address>

  <p class="cta">
    <span class="cta__label">LEARN MORE AT</span>
    <span class="cta__url">larkspur-stillness.com</span>
  </p>
</main>
</body>
</html>
```